Plastic Surgeon Stationary Design

I Already have the logo. I Want and a clean, minimalist and elegant project. Please, I prefer Black, White and Gold color but you're free to try another ones. Business card,
Letterhead (A4 and Office), Recipes (Letter Pad) (A5), Envelop, Invoice, Computer Bill, Bill Book, Single A4 page size,
You Have to create at least the same materials I already own. I would like to a file to use in word to print letterheads and letter pad.
What I want that you make more changes are the envelopes that are to colorful and not elegant.
I'll not accept any design without my addresses as you can guide yourself with the models I provide.
Here are the addresses too:
"www.rubemtavorasilva.example" (website)
(My clinics' address)
"SÃO PAULO
Rua Lucas Bentim, 3180, Lucas Bentim Office, Cj 204
São Paulo - SP
(11) 90123-4567"
"BALNEÁRIO CAMBORIÚ
Rua Clemente Vilaça, 418, 7° andar
Edificio Torre Quaresma
Balneário Camboriú - SC
(047) 9012-3456"
Attention: Letterheads, Recipes, have to contain "CRM/SC 52.807 and CRM/SP 308.614" close to my name (Dr. Rubem Távora - Cirurgião Plástico), it is usually placed at the bottom.
Designers, attention!
During the process of creating bear in mind that the details of the logo, as the faces on the sides, are designed to be subtle. Highlight other such details affect the delicacy and elegance of the logo and visual identity.
When you are creating stationery, do not abuse the use of the logo, it should be used once or at most two times in each item.
Remember! Each stationery set must submit 3 models, one with the address "Balneario Camboriu", another with the address of "São Paulo" and the third containing both addresses.
The model letter envelope, folder type bag for letterhead and folder with inner pocket that provided a model did not please me because they are very flashy. Give preference to the use of white or black background.
PLEASE! Seek inspiration in the models contained in this link:
https://www.filecrate.example/sh/kq27zp41wcx905m/PlRtVuY_QX
In this link you can find my PAST Stationary Itens, so it can help you on your work
https://docuvault.example/7ZK3NB8QeT2LwYhR
Reason: Nobody presented anything useful.
Reason: still waiting some designers send their projects
Reason: Still Waiting Some Designs....
Target Market(s)
Mostly females with good economical condition. (Class A and AB)
Industry/Entity Type
Business
Requirements
Must have
- You have to provide 3 models of each paper, one with the address of São Paulo, another with the Balneario Camboriú address, and the third one with both addresses.

```html
<!DOCTYPE html>
<html lang="pt-BR">
<head>
<meta charset="utf-8">
<title>Rubem Távora – Papelaria</title>
<link rel="stylesheet" href="https://fonts.googleapis.com/css2?family=Playfair+Display:wght@500&family=Open+Sans:wght@400;600&display=swap">
<style>
  :root{
    --backdrop:#cdcdcd;
    --paper:#f7f7f7;
    --gold:#b28b4f;
    --gold-light:#dcc08a;
    --gold-dark:#a17a3f;
    --ink:#3a3a3a;
    --rule:#e2e2e2;
    --divider:#bdbdbd;
  }
  *{margin:0;padding:0;box-sizing:border-box}
  html,body{width:1200px;height:777px;overflow:hidden}
  body{background:var(--backdrop);position:relative;font-family:"Open Sans",Arial,sans-serif;color:var(--ink)}
  .sheet{position:absolute;background:var(--paper)}
  .letterhead{left:321px;top:101px;width:270px;height:381px}
  .folder{left:623px;top:101px;width:281px;height:396px}
  .envelope-front{left:258px;top:529px;width:310px;height:135px;overflow:hidden}
  .envelope-back{left:596px;top:529px;width:309px;height:135px}

  .brand-name{font-family:"Playfair Display",Georgia,serif;font-weight:500;color:var(--gold);white-space:nowrap;position:absolute;left:0;right:0;text-align:center}
  .letterhead .brand-name{top:12px;font-size:17px}
  .envelope-front .brand-name{top:63px;font-size:16px}
  .envelope-back .brand-name{top:16px;font-size:8px}

  .gold-panel{position:absolute;background:linear-gradient(90deg,var(--gold-dark),var(--gold-light) 60%,var(--gold))}
  .letterhead .gold-panel{top:0;width:14px;height:42px}
  .letterhead .gold-panel.left{left:0}
  .letterhead .gold-panel.right{right:0}
  .envelope-front .gold-panel{top:0;height:135px}
  .envelope-front .gold-panel.left{left:0;width:42px}
  .envelope-front .gold-panel.right{right:0;width:44px}

  .footer{position:absolute;text-align:center;line-height:1.3;white-space:nowrap}
  .registry{display:block;letter-spacing:.02em}
  .clinics{display:flex;justify-content:center;align-items:flex-start;margin-top:.6em}
  .clinic{flex:0 0 auto}
  .clinic.sp{text-align:right;padding-right:.8em}
  .clinic.bc{text-align:left;padding-left:.8em}
  .clinic strong{font-weight:600;display:block}
  .footer-mark{flex:0 0 auto;font-family:"Playfair Display",Georgia,serif;color:var(--gold);white-space:nowrap;padding:0 .4em;align-self:center}
  .website{display:block;margin-top:.5em}

  /* small footers set at double size and scaled down, so tiny text keeps its proportions */
  .letterhead .footer{top:340px;left:-135px;width:540px;font-size:7.2px;transform:scale(.5);transform-origin:50% 0}
  .folder .footer{top:337px;left:0;right:0;font-size:5px}
  .envelope-back .footer{top:102px;left:-154.5px;width:618px;font-size:6.6px;transform:scale(.5);transform-origin:50% 0}
  .envelope-back .clinic.bc{border-left:1px solid var(--divider)}
  .envelope-back .clinics{margin-top:0}

  .folder-flap{position:absolute;left:0;right:0;top:44px;border-top:1px solid var(--rule)}
  .folder-closure{position:absolute;left:130px;top:14px}
</style>
</head>
<body>

  <section class="sheet letterhead" aria-label="Papel timbrado">
    <div class="gold-panel left" role="img" aria-label="Faixa dourada com perfil de rosto"></div>
    <div class="gold-panel right" role="img" aria-label="Faixa dourada com perfil de rosto"></div>
    <div class="brand-name">Rubem Távora</div>
    <div class="footer">
      <span class="registry">CRM/SP 308.614 &nbsp;|&nbsp; CRM/SC 52.807</span>
      <div class="clinics">
        <div class="clinic sp"><strong>SÃO PAULO</strong>Rua Lucas Bentim, 3180<br>Lucas Bentim Office, Cj 204<br>São Paulo - SP<br>(11) 90123-4567</div>
        <span class="footer-mark">Rubem Távora</span>
        <div class="clinic bc"><strong>BALNEÁRIO CAMBORIÚ</strong>Rua Clemente Vilaça, 418, 7° andar<br>Edificio Torre Quaresma<br>Balneário Camboriú - SC<br>(047) 9012-3456</div>
      </div>
      <span class="website">www.rubemtavorasilva.example</span>
    </div>
  </section>

  <section class="sheet folder" aria-label="Envelope saco">
    <div class="folder-flap"></div>
    <svg class="folder-closure" width="24" height="80" viewBox="0 0 24 80" aria-hidden="true">
      <circle cx="12" cy="10" r="7" fill="#fafafa" stroke="#dddddd"/>
      <circle cx="12" cy="70" r="7" fill="#fafafa" stroke="#dddddd"/>
      <path d="M12 12 L8 40 L14 52 L12 68" fill="none" stroke="#d6d6d6" stroke-width="1"/>
    </svg>
    <div class="footer">
      <span class="registry">CRM/SP 308.614 &nbsp;|&nbsp; CRM/SC 52.807</span>
      <div class="clinics">
        <div class="clinic sp"><strong>SÃO PAULO</strong>Rua Lucas Bentim, 3180<br>Lucas Bentim Office, Cj 204<br>São Paulo - SP<br>(11) 90123-4567</div>
        <span class="footer-mark">Rubem Távora</span>
        <div class="clinic bc"><strong>BALNEÁRIO CAMBORIÚ</strong>Rua Clemente Vilaça, 418, 7° andar<br>Edificio Torre Quaresma<br>Balneário Camboriú - SC<br>(047) 9012-3456</div>
      </div>
      <span class="website">www.rubemtavorasilva.example</span>
    </div>
  </section>

  <section class="sheet envelope-front" aria-label="Envelope carta, frente">
    <div class="gold-panel left" role="img" aria-label="Painel dourado com perfil de rosto"></div>
    <div class="gold-panel right" role="img" aria-label="Painel dourado com perfil de rosto"></div>
    <div class="brand-name">Rubem Távora</div>
  </section>

  <section class="sheet envelope-back" aria-label="Envelope carta, verso">
    <div class="brand-name">Rubem Távora</div>
    <div class="footer">
      <div class="clinics">
        <div class="clinic sp"><strong>SÃO PAULO</strong>Rua Lucas Bentim, 3180<br>Lucas Bentim Office, Cj 204<br>São Paulo - SP<br>(11) 90123-4567</div>
        <div class="clinic bc"><strong>BALNEÁRIO CAMBORIÚ</strong>Rua Clemente Vilaça, 418, 7° andar<br>Edificio Torre Quaresma<br>Balneário Camboriú - SC<br>(047) 9012-3456</div>
      </div>
      <span class="website">www.rubemtavorasilva.example</span>
    </div>
  </section>

</body>
</html>
```